Mental Health

QRT HAVEN
Behavioral Health
4172 W. Pell St. Mesa, AZ 85219
Gwendolyn (480)555-0142 / Omar 480-555-0187

Email: QRTHaven@Mailvex.example
Newly Remodeled & Spacious
g Staff
Registered Nurses
Licensed Independent &
Professional Substance &
Abuse Counselors
Behavioral Health Techs
Certified Caregivers
Behavioral Health &
Substance Abuse Professionals

To Refer a Patient
About Us
QRT Haven is a Fully Staffed Behavioral
Health Residential Facility, providing
treatment plans for adults suffering
with various Behavioral Health and
Substance Abuse disorders, while living
in a nice safe, clean and supportive
environment. Our home offers clients the
ability to learn the necessary skills to
help clients adapt, build self confidence
as well as independence, with the goal
of reducing the probability of a future
crisis or possible relapse. We offer
counseling programs, consisting of a
variety of addiction and recovery support
groups, independent living, coping and
social skills groups, as well as assisting
clients with using tools to create a resume
to help obtain employment and so much
more. We are committed to teaching
self management care and allowing
clients to understand how to utilize the
resources, skills and tools available for
long term success by providing superior
quality, all-inclusive living arrangements
and treatment options.

Thank you for your patience while I update the final content needed for us to make the final decision this week.

```html
<!DOCTYPE html>
<html lang="en">
<head>
<meta charset="utf-8">
<title>QRT Haven Business Card</title>
<link href="https://fonts.googleapis.com/css2?family=Roboto:wght@400;500;700&display=swap" rel="stylesheet">
<style>
  :root {
    --page-bg: #9a9a9a;
    --card-white: #ffffff;
    --brand-blue: #1a6fbe;
    --back-blue: #0870bb;
    --phone-green: #7ab42c;
    --text-grey: #555555;
    --emblem-light: #2fd0f5;
    --emblem-deep: #1446b8;
    --art-grey: #6a6a6a;
    --art-warm: #f3c9d6;
    --art-cool: #cfe2f3;
  }
  html, body {
    margin: 0;
    padding: 0;
    width: 1200px;
    height: 1200px;
    overflow: hidden;
    background: var(--page-bg);
    font-family: "Roboto", Arial, sans-serif;
  }
  .card {
    position: absolute;
    left: 262px;
    width: 686px;
    height: 392px;
    border-radius: 22px;
    overflow: hidden;
  }
  .card--front { top: 165px; background: var(--card-white); }
  .card--back { top: 653px; background: var(--back-blue); }

  .brand {
    position: absolute;
    left: 35px;
    top: 42px;
    display: flex;
    align-items: center;
    gap: 12px;
  }
  .brand__dot {
    width: 56px;
    height: 56px;
    border-radius: 50%;
    background: var(--brand-blue);
  }
  .brand__name {
    font-size: 34px;
    font-weight: 400;
    color: var(--brand-blue);
    letter-spacing: 1px;
  }

  .front-art {
    position: absolute;
    left: 290px;
    top: 32px;
    width: 378px;
    height: 360px;
    border-radius: 180px 180px 0 0;
    background:
      radial-gradient(ellipse at 50% 30%, rgba(106,106,106,0.35), rgba(106,106,106,0) 55%),
      linear-gradient(90deg, var(--art-cool), var(--art-warm) 50%, var(--art-cool));
    opacity: 0.8;
  }

  .contacts {
    position: absolute;
    left: 34px;
    top: 140px;
    line-height: 1.25;
  }
  .contact { margin-bottom: 12px; }
  .contact__name {
    font-size: 19px;
    font-weight: 700;
    color: var(--brand-blue);
  }
  .contact__phone {
    font-size: 16px;
    color: var(--phone-green);
  }
  .company {
    margin-top: 6px;
    font-size: 16px;
    line-height: 1.3;
    color: var(--brand-blue);
  }
  .address {
    font-size: 16px;
    color: var(--text-grey);
    line-height: 1.3;
  }
  .email {
    margin-top: 20px;
    font-size: 16px;
    color: var(--text-grey);
  }

  .back-brand {
    position: absolute;
    left: 0;
    right: 0;
    top: 68px;
    display: flex;
    flex-direction: column;
    align-items: center;
    gap: 14px;
  }
  .back-brand__dot {
    width: 130px;
    height: 130px;
    border-radius: 50%;
    background: linear-gradient(135deg, var(--emblem-light), var(--emblem-deep));
  }
  .back-brand__name {
    font-size: 26px;
    font-weight: 500;
    color: #ffffff;
    letter-spacing: 1px;
  }
  .services {
    position: absolute;
    left: 0;
    right: 0;
    top: 281px;
    text-align: center;
    color: #ffffff;
    font-size: 16px;
    line-height: 1.22;
  }
  .services__tick {
    display: inline-block;
    vertical-align: -2px;
    margin: 0 4px;
  }
</style>
</head>
<body>
  <section class="card card--front">
    <div class="brand">
      <div class="brand__dot"></div>
      <div class="brand__name">QRT HAVEN</div>
    </div>
    <div class="front-art" role="img" aria-label="Large decorative brand emblem area"></div>
    <div class="contacts">
      <div class="contact">
        <div class="contact__name">GWENDOLYN</div>
        <div class="contact__phone">(480)555-0142</div>
      </div>
      <div class="contact">
        <div class="contact__name">OMAR</div>
        <div class="contact__phone">480-555-0187</div>
      </div>
      <div class="company">QRT HAVEN<br>Behavioral Health</div>
      <div class="address">4172 W. Pell St. Mesa, AZ 85219</div>
      <div class="email">QRTHaven@Mailvex.example</div>
    </div>
  </section>

  <section class="card card--back">
    <div class="back-brand">
      <div class="back-brand__dot"></div>
      <div class="back-brand__name">QRT HAVEN</div>
    </div>
    <div class="services">
      Newly Remodeled &amp; Spacious Staff Registered Nurses<br>
      Licensed Independent &amp; Professional Substance &amp; Abuse Counselors<br>
      Behavioral Health Techs
      <svg class="services__tick" width="15" height="15" viewBox="0 0 16 16" aria-hidden="true">
        <circle cx="8" cy="8" r="8" fill="#ffffff"/>
        <path d="M4.5 8.2 L7 10.6 L11.6 5.6" fill="none" stroke="#0870bb" stroke-width="2"/>
      </svg>
      Certified Caregivers<br>
      Behavioral Health &amp; Substance Abuse Professionals
    </div>
  </section>
</body>
</html>
```